New Facebook Banner

Hi
We are operating Ramen shop in Australia.(http://mizunokobowls.com)
I want to create new design for our Facebook banner and title is "Free Ramen on your Birthday".
Sample attached is our existing banner design. We would like to make it more modern and sophisticated.
We are so looking forward to seeing your design for our free ramen promotion.

https://www.facebook.com/mizunokobowls/

Industry/Entity Type

Japanese Restaurant

Font styles to use
Sans Serif

```html
<!DOCTYPE html>
<html lang="en">
<head>
<meta charset="utf-8">
<title>Free Ramen on Your Birthday – Social Banner</title>
<link rel="stylesheet" href="https://fonts.googleapis.com/css2?family=Luckiest+Guy&family=Open+Sans:wght@400&display=block">
<style>
  :root {
    --bg-deep: #241449;
    --bg-mid: #33206a;
    --cyan: #3fdcef;
    --cyan-depth: #1784a8;
    --magenta: #e43ccb;
    --magenta-depth: #8a1b86;
    --outline: #ffffff;
    --caption-bg: #ffffff;
    --caption-ink: #2a2a2a;
  }
  html, body {
    margin: 0;
    padding: 0;
    overflow: hidden;
    background: var(--bg-deep);
  }
  .banner {
    position: relative;
    width: 1200px;
    height: 444px;
    overflow: hidden;
  }
  .party-pattern {
    position: absolute;
    inset: 0;
    background: radial-gradient(ellipse at 50% 50%, var(--bg-mid) 0%, var(--bg-deep) 75%);
  }
  .headline {
    position: absolute;
    left: 0;
    right: 0;
    margin: 0;
    text-align: center;
    white-space: nowrap;
    text-transform: uppercase;
    font-family: "Luckiest Guy", Impact, sans-serif;
    font-weight: 400;
    line-height: 1;
    letter-spacing: 2px;
    -webkit-text-stroke: 8px var(--outline);
    paint-order: stroke fill;
  }
  .headline--top {
    top: 118px;
    font-size: 110px;
    color: var(--cyan);
    text-shadow:
      0 3px 0 var(--outline),
      0 7px 0 var(--cyan-depth),
      0 10px 0 var(--cyan-depth),
      0 14px 10px rgba(0, 0, 0, 0.45);
  }
  .headline--bottom {
    top: 232px;
    font-size: 114px;
    color: var(--magenta);
    text-shadow:
      0 3px 0 var(--outline),
      0 7px 0 var(--magenta-depth),
      0 10px 0 var(--magenta-depth),
      0 14px 10px rgba(0, 0, 0, 0.45);
  }
  .caption {
    position: absolute;
    left: 318px;
    top: 374px;
    width: 564px;
    height: 39px;
    margin: 0;
    box-sizing: border-box;
    background: var(--caption-bg);
    color: var(--caption-ink);
    font-family: "Open Sans", Arial, sans-serif;
    font-size: 19px;
    line-height: 39px;
    text-align: center;
    white-space: nowrap;
  }
</style>
</head>
<body>
  <div class="banner">
    <div class="party-pattern" role="img" aria-label="Neon party pattern of birthday cakes, balloons, gift boxes, party hats, candies, stars and streamers in cyan, pink and yellow on deep purple"></div>
    <h1 class="headline headline--top">Free Ramen</h1>
    <p class="headline headline--bottom">On Your Birthday</p>
    <p class="caption">To find more, please visit: http://mizunokobowls.com/</p>
  </div>
</body>
</html>
```